Pagepress Design Project

We are looking for a new design for our website - and need your help to make it great.

Our current website is here: http://www.morvela.com: It has way too much information on it and it lacks a clear focus.

You can download the current design approach here: http://qx.zp/kLp82rwdna

It is a layered PSD file with the various approved images for the different sections. We have also uploaded images to the project which you can use.

Please use these section images in your designs with improvement suggestions as per below.

What we still need:

Header: We are not entirely sure about the header yet - variations for this would be great.

Colour scheme: We are not sure about the colour scheme yet: if you have better ideas, please present them. May be less colours, or muted colours ?

Improvements required to section images:

Full design Freedom: The monitor with t-shirts is fine, the middle screen should be a gallery of modern watches (image provided or you can create a better one) and the fruits - image provided (see attached image Morvela_site_development_blue-header)

Many product types: really only the text in the bubbles needs some improvements

Main Website Font:

The font in the supplied PSD file is a Plimbo web font called Open Sans http://www.plimbo.com/fonts/specimen/Open+Sans

This font is quite nice, but not so easy to read on some backgrounds. It can be replaced with a stronger font which does not look too heavy or playful.

Font for: "Click on any T-Shirt to see how it works": http://www.brondwick.com.au/type/sketch.html. If you can think of a nicer handwritten code you are welcome - I am happy with this one.

we are also lacking the additional page designs - content, blog, contact, pricing and so on.

We are quite far down the track with this design - only participate if you think you can create a genuinely better and stronger approach.

Target Market(s)

Designers and small business owners

Industry/Entity Type

Plimbo

Requirements
Must have
• Home page (improvement of current approach)
Note that text and section images are approved apart from those listed above - so only create others if you can do genuinely better
content page
contact page
A better footer
blog design
pricing page
Nice to have
• anything else you can come up with to make the site look more appealing and professional.

We only need designs - and layered psd files - programming will be a separate task
Should not have
• Photos which are TOO stock style. We use pixharbor and snaprova

```html
<!DOCTYPE html>
<html lang="en">
<head>
<meta charset="utf-8">
<title>Morvela – eCommerce Solution</title>
<link href="https://fonts.googleapis.com/css2?family=Arimo:wght@400;700&display=swap" rel="stylesheet">
<style>
:root{
  --blue:#0e6fbd;
  --title-blue:#1a6bbd;
  --orange:#ff5a00;
  --green:#5aab14;
  --lime:#7cbd1b;
  --text:#3c3c3c;
  --line:#e4e4e4;
  --panel:#f3f3f3;
  --footer-soft:#9cc9ee;
}
*{margin:0;padding:0;box-sizing:border-box}
html,body{width:842px;height:1200px;overflow:hidden;background:#fff}
body{position:relative;font-family:"Arimo",Arial,sans-serif;color:var(--text)}
a{color:inherit;text-decoration:none}
h1,h2,h4{font-weight:400}
.abs{position:absolute}

.top-rule{left:0;top:0;width:842px;height:3px;background:var(--lime)}
.brand{left:107px;top:26px;font-size:24px;font-weight:700;color:var(--blue);letter-spacing:-.5px;z-index:3}
.nav{left:401px;top:39px;display:flex;align-items:center;font-size:10px;color:#444;z-index:3}
.nav a{margin-right:18px;line-height:21px}
.nav .register{background:var(--green);color:#fff;padding:0 9px;height:21px;line-height:21px;margin-left:-4px;margin-right:0;border-radius:1px}

.hero{left:0;top:70px;width:842px;height:301px;background:var(--blue)}
.hero-title{left:107px;top:128px;width:290px;font-size:25px;font-weight:700;line-height:26px;color:#fff}
.hero-copy{left:107px;top:191px;width:238px;font-size:9.4px;line-height:13.4px;color:#fff}
.btn-orange{background:var(--orange);color:#fff;display:flex;align-items:center;justify-content:center}
.hero-cta{left:107px;top:270px;width:230px;height:36px;font-size:14px;border:1px solid #fff}
.hero-visual{left:384px;top:70px;width:458px;height:320px;z-index:1;
  background:linear-gradient(100deg,#dfe5ea 0%,#c9d2da 55%,#e7c3b6 80%,#e84a7b 100%)}

.partners{left:107px;top:418px;width:630px;display:flex;justify-content:space-between;font-size:11px;font-weight:700;color:#a5a5a5}
.rule{left:0;width:842px;height:1px;background:var(--line);box-shadow:0 1px 2px rgba(0,0,0,.05)}

.sec-title{font-size:14px;color:var(--title-blue)}
.intro-copy{left:107px;top:516px;width:225px;font-size:9.2px;line-height:13.4px;color:#444}
.intro-copy p+p{margin-top:13px}
.start-panel{left:107px;top:610px;width:243px;height:88px;background:var(--panel)}
.start-panel .label{position:absolute;left:31px;top:15px;font-size:12px;color:#555}
.tour-big{position:absolute;left:20px;top:37px;width:202px;height:35px;background:var(--green);color:#fff;font-size:20px;display:flex;align-items:center;justify-content:center}
.video-title{left:464px;top:487px}
.video-card{left:364px;top:513px;width:381px;height:191px;border:1px solid #e2e2e2;box-shadow:0 1px 4px rgba(0,0,0,.12);
  background:linear-gradient(180deg,#b23a2a 0 8px,#f4f4f4 8px 28px,#fff 28px 50px,#f6e6b8 50px 64px,#fbfaf5 64px)}
.play{left:524px;top:575px;width:64px;height:64px}

.why-title{left:0;top:746px;width:842px;text-align:center;font-size:21px;font-weight:700;color:var(--title-blue)}
.features{left:108px;top:788px;display:flex;gap:6.5px}
.feature{width:120px;height:150px;border:1px solid #d6d6d6;text-align:center;display:flex;flex-direction:column;align-items:center;padding-top:13px}
.feature svg{width:64px;height:66px}
.feature p{margin-top:8px;font-size:10px;line-height:13px;color:#777;width:100px;letter-spacing:.2px}

.cta-row{left:205px;top:975px;height:36px;display:flex;align-items:center;font-size:16px;color:#444}
.cta-row .btn{height:36px;padding:0 13px;font-size:14px;color:#fff;display:flex;align-items:center}
.cta-row .start{background:var(--orange);margin-left:19px}
.cta-row .or{margin:0 9px}
.cta-row .tour{background:var(--green)}

.footer{left:0;top:1029px;width:842px;height:171px;background:var(--blue)}
.foot-col{top:1052px;font-size:8px;line-height:13.3px;color:#fff}
.foot-col h4{font-size:9.5px;font-weight:700;margin-bottom:2px;letter-spacing:.2px}
.foot-brand{left:594px;top:1064px;font-size:25px;font-weight:700;color:#fff;letter-spacing:-.5px}
.foot-tag{left:589px;top:1096px;font-size:9px;font-weight:700;color:var(--footer-soft)}
.foot-rule{left:0;top:1146px;width:842px;height:1px;background:rgba(255,255,255,.25)}
.legal{left:112px;top:1156px;font-size:6.5px;color:#fff}
</style>
</head>
<body>
<div class="abs top-rule"></div>

<header>
  <div class="abs brand">morvela</div>
  <nav class="abs nav">
    <a href="#">Home</a><a href="#">Tour</a><a href="#">Pricing</a><a href="#">Contact</a><a href="#">Log in</a>
    <a href="#" class="register">Register</a>
  </nav>
</header>

<section>
  <div class="abs hero"></div>
  <h1 class="abs hero-title">The last eCommerce solution you'll need</h1>
  <p class="abs hero-copy">Accept orders from your website, Friendloop, Pinboardly, a Pagepress blog, your Morvela store, eMail, Chirply, Callwave, SMS, a printed broshures, magazines, radio and TV. Zero programming, total design freedom.</p>
  <a href="#" class="abs btn-orange hero-cta">It's free! Start here</a>
  <div class="abs hero-visual" role="img" aria-label="Desktop monitor showing a fresh produce sample store, with a shopper holding shopping bags"></div>
</section>

<div class="abs partners">
  <span>Paynest</span><span>Trustmark</span><span>Ledgero</span><span>Tranzo</span><span>Shipwell</span><span>Expedo</span><span>Parcelo</span><span>Bookwise</span><span>Friendloop</span><span>Pagepress</span><span>Vidcast</span><span>Pinboardly</span>
</div>
<div class="abs rule" style="top:456px"></div>

<section>
  <h2 class="abs sec-title" style="left:107px;top:487px">Simple Solutions, Powerful Results</h2>
  <div class="abs intro-copy">
    <p>Now you can have kick-ass eCommerce with zero programming. Start selling from anywhere you want in under 60 seconds.</p>
    <p>Its almost like magic.</p>
  </div>
  <div class="abs start-panel">
    <span class="label">Get Started with Morvela Today.</span>
    <a href="#" class="tour-big">Take a Tour</a>
  </div>
  <h2 class="abs sec-title video-title">Watch Video to learn more..</h2>
  <svg class="abs" style="left:638px;top:486px" width="16" height="22" viewBox="0 0 16 22"><path d="M2 2c8 2 11 8 8 16" fill="none" stroke="#5aab14" stroke-width="2"/><path d="M5 15l5 5 3-6" fill="none" stroke="#5aab14" stroke-width="2"/></svg>
  <div class="abs video-card" role="img" aria-label="Video preview of a restaurant menu page with appetizer dishes"></div>
  <svg class="abs play" viewBox="0 0 64 64"><circle cx="32" cy="32" r="28" fill="rgba(0,0,0,.15)" stroke="#fff" stroke-width="4"/><path d="M26 20l18 12-18 12z" fill="#fff"/></svg>
</section>
<div class="abs rule" style="top:717px"></div>

<section>
  <h2 class="abs why-title">Why You'll love Morvela</h2>
  <div class="abs features">
    <div class="feature">
      <svg viewBox="0 0 64 66"><rect x="6" y="22" width="52" height="42" rx="2" fill="#0e6fbd"/><path d="M18 26V12a7 7 0 0114 0v14M32 26V12a7 7 0 0114 0v14" fill="none" stroke="#0e6fbd" stroke-width="5"/><path d="M32 22v42" stroke="#fff" stroke-width="2"/></svg>
      <p>Sell Physical Products &amp; Services</p>
    </div>
    <div class="feature">
      <svg viewBox="0 0 80 66"><circle cx="24" cy="33" r="22" fill="#0e6fbd"/><circle cx="24" cy="33" r="8" fill="none" stroke="#fff" stroke-width="2.5"/><circle cx="24" cy="33" r="2.5" fill="#fff"/><path d="M42 12h26l8 8v36H42z" fill="#0e6fbd" stroke="#fff" stroke-width="2"/><text x="47" y="42" font-family="Arimo,Arial,sans-serif" font-size="13" font-style="italic" fill="#fff">PDF</text></svg>
      <p>Offer Music, Videos, eBooks, Photos &amp; more</p>
    </div>
    <div class="feature">
      <svg viewBox="0 0 64 66"><circle cx="32" cy="18" r="14" fill="#ff5a00"/><circle cx="18" cy="28" r="12" fill="#ff5a00"/><circle cx="46" cy="28" r="12" fill="#ff5a00"/><circle cx="32" cy="34" r="11" fill="#ff5a00"/><path d="M28 38h8l2 22 6 5H20l6-5z" fill="#ff5a00"/></svg>
      <p>Quickly create donation drives and fundraisers</p>
    </div>
    <div class="feature">
      <svg viewBox="0 0 64 66"><g transform="rotate(-35 32 33)"><path d="M6 20h52v8a5 5 0 000 10v8H6v-8a5 5 0 000-10z" fill="#0e6fbd"/><rect x="16" y="25" width="32" height="16" fill="none" stroke="#fff" stroke-width="3"/></g></svg>
      <p>Sell and scan admission tickets for your events</p>
    </div>
    <div class="feature">
      <svg viewBox="0 0 64 66"><path d="M16 28L30 10h4l14 18" fill="none" stroke="#0e6fbd" stroke-width="4"/><path d="M4 26h56l-4 8H8z" fill="#0e6fbd"/><path d="M10 36h44l-6 20H16z" fill="#0e6fbd"/><path d="M22 40v12M29 40v12M36 40v12M43 40v12" stroke="#fff" stroke-width="3"/></svg>
      <p>Sell subscription services and collect regular fees</p>
    </div>
  </div>
</section>
<div class="abs rule" style="top:955px"></div>

<div class="abs cta-row">
  <span>Get started in 45 seconds</span>
  <a href="#" class="btn start">Start here</a>
  <span class="or">or</span>
  <a href="#" class="btn tour">Take a Tour</a>
</div>

<footer>
  <div class="abs footer"></div>
  <div class="abs foot-col" style="left:112px"><h4>PRODUCT</h4><div>Tour</div><div>Success Stories</div><div>Pricing</div><div>Security</div><div>Login</div></div>
  <div class="abs foot-col" style="left:214px"><h4>COMPANY</h4><div>About</div><div>Careers</div><div>Valued Partner Program</div><div>Press</div><div>Blog</div></div>
  <div class="abs foot-col" style="left:341px"><h4>HELP &amp; SUPPORT</h4><div>Support Center</div><div>Idea Board</div><div>Developer Tools</div><div>Forgotten Password</div><div>Contact Us</div></div>
  <div class="abs foot-col" style="left:472px"><h4>COMMUNITY</h4><div>Friendloop</div><div>Chirply</div><div>Linkwise</div><div>Plimbo+</div></div>
  <div class="abs foot-brand">morvela</div>
  <div class="abs foot-tag">eCommerce Solution</div>
  <div class="abs foot-rule"></div>
  <div class="abs legal">© 2013 Morvela. All rights reserved. &nbsp;| &nbsp;Privacy &nbsp;| &nbsp;Terms of Use</div>
</footer>
</body>
</html>
```